Business Card For Construction Company
Falcon Erectors
Business Card For Construction Company - Construction
Creative Brief
Professional
Pavel Lunov
No Address
PavelLunov@FalconErectorsCorp.example
www.FalconErectorsCorp.example

```html
<!DOCTYPE html>
<html lang="en">
<head>
<meta charset="utf-8">
<title>Falcon Erectors – Business Card</title>
<link href="https://fonts.googleapis.com/css2?family=Exo+2:wght@500;700;800&display=swap" rel="stylesheet">
<style>
  :root {
    --backdrop: #c9cacc;
    --card-white: #ffffff;
    --brand-blue: #1766ad;
    --brand-blue-light: #2f8fd6;
    --brand-blue-dark: #0b4a86;
    --band-grey: #8d9196;
    --faint-blue: #dbe6f1;
    --ink-white: #ffffff;
  }
  html, body {
    margin: 0;
    padding: 0;
    width: 1200px;
    height: 895px;
    overflow: hidden;
    background: var(--backdrop);
    font-family: "Exo 2", sans-serif;
  }
  .canvas {
    position: relative;
    width: 1200px;
    height: 895px;
  }
  .card {
    position: absolute;
    top: 287px;
    width: 540px;
    height: 320px;
    background: var(--card-white);
    box-shadow: 0 6px 18px rgba(0,0,0,0.18);
    overflow: hidden;
  }
  .card--back { left: 40px; }
  .card--front { left: 620px; }
  .card svg.card-art {
    position: absolute;
    inset: 0;
  }
  .holder-name {
    position: absolute;
    left: 30px;
    top: 30px;
    margin: 0;
    color: var(--ink-white);
    font-weight: 500;
    font-size: 15px;
    letter-spacing: 1.5px;
    font-variant: small-caps;
  }
  .contact-list {
    position: absolute;
    left: 30px;
    top: 190px;
    margin: 0;
    padding: 0;
    list-style: none;
    color: var(--ink-white);
    font-size: 10.5px;
    letter-spacing: 0.6px;
    line-height: 19px;
  }
  .contact-list li {
    display: flex;
    align-items: center;
    gap: 7px;
  }
  .contact-list svg { flex: none; }
  .wordmark {
    position: absolute;
    display: flex;
    align-items: center;
    gap: 10px;
    color: var(--brand-blue);
    font-weight: 800;
    text-transform: uppercase;
    white-space: nowrap;
  }
  .wordmark__square {
    background: var(--brand-blue);
    flex: none;
  }
  .card--back .wordmark {
    left: 318px;
    top: 190px;
    font-size: 19px;
    letter-spacing: 0.5px;
  }
  .card--back .wordmark__square { width: 22px; height: 22px; }
  .card--front .wordmark {
    right: 34px;
    top: 196px;
    font-size: 24px;
    letter-spacing: 0.5px;
  }
  .card--front .wordmark__square { width: 28px; height: 28px; }
  .faint-mark {
    position: absolute;
    left: 90px;
    top: 40px;
    width: 190px;
    height: 190px;
    background: var(--faint-blue);
    opacity: 0.8;
  }
</style>
</head>
<body>
<main class="canvas">

  <section class="card card--back" aria-label="Card back with contact details">
    <svg class="card-art" width="540" height="320" viewBox="0 0 540 320">
      <defs>
        <radialGradient id="panelBlue" cx="0.35" cy="0.4" r="0.8">
          <stop offset="0" stop-color="#2f8fd6"/>
          <stop offset="0.6" stop-color="#1766ad"/>
          <stop offset="1" stop-color="#0b4a86"/>
        </radialGradient>
      </defs>
      <path d="M0 0 H300 C262 100 262 220 300 320 H0 Z" fill="#8d9196"/>
      <path d="M0 0 H284 C246 100 246 220 284 320 H0 Z" fill="url(#panelBlue)"/>
    </svg>
    <h1 class="holder-name">Pavel Lunov</h1>
    <ul class="contact-list">
      <li>
        <svg width="9" height="9" viewBox="0 0 10 10"><path d="M2 1 L4 1 L4.6 3 L3.4 4 Q4.5 6 6 6.6 L7 5.4 L9 6 L9 8 Q8 9.2 6.5 8.8 Q2 7.2 1 3 Q0.8 1.8 2 1 Z" fill="#fff"/></svg>
        555-014-2290
      </li>
      <li>
        <svg width="9" height="9" viewBox="0 0 10 10"><path d="M2 1 L4 1 L4.6 3 L3.4 4 Q4.5 6 6 6.6 L7 5.4 L9 6 L9 8 Q8 9.2 6.5 8.8 Q2 7.2 1 3 Q0.8 1.8 2 1 Z" fill="#fff"/></svg>
        555-019-7730
      </li>
      <li>
        <svg width="9" height="9" viewBox="0 0 10 10"><rect x="0.5" y="2" width="9" height="6" fill="none" stroke="#fff"/><path d="M0.5 2 L5 5.5 L9.5 2" fill="none" stroke="#fff"/></svg>
        PavelLunov@FalconErectorsCorp.example
      </li>
      <li>
        <svg width="9" height="9" viewBox="0 0 10 10"><circle cx="5" cy="5" r="4.3" fill="none" stroke="#fff"/><path d="M0.7 5 H9.3 M5 0.7 Q2.5 5 5 9.3 M5 0.7 Q7.5 5 5 9.3" fill="none" stroke="#fff" stroke-width="0.8"/></svg>
        www.FalconErectorsCorp.example
      </li>
    </ul>
    <div class="wordmark"><span class="wordmark__square"></span>Falcon Erectors</div>
  </section>

  <section class="card card--front" aria-label="Card front with company name">
    <div class="faint-mark"></div>
    <div class="wordmark"><span class="wordmark__square"></span>Falcon Erectors</div>
  </section>

</main>
</body>
</html>
```